New Business Card Design Project

We are looking for a talented individual to create a truly awesome/unique business card design for us. We are looking for a someone to design something that will really stand out from the crowd - we don't mind what ideas you come up with (ie embossed/flat/matte/shine etc etc) just wow us with your creativity.
Updates

Target Market(s)

Video Games Industry Professionals (all levels of seniority from QA Testers through to CEOs)

Contact Information for Business Card

Company logo (see upload)
Company name: Northbay Play Careers Ltd
Employee Name: Darren Elsby
Job title: CEO
Website: www.nbpc2go.example
Office +44 1632 960418
Mobile: +44 7700 900276
Email: darren@nbpc2go.example

Colors

Designer to choose colors to be used in the design.

Requirements
Must have
• The business card design MUST contain all the information listed in the BUSINESS CARD DETAILS box.
• You will see the colours that are relevant to us (ie company logo) in the uploaded imagery - however you do not have to use all these colours when designing the business card itself
• MUST BE DOUBLE SIDED

```html
<!DOCTYPE html>
<html lang="en">
<head>
<meta charset="utf-8">
<title>Northbay Play Careers – Business Card</title>
<link href="https://fonts.googleapis.com/css2?family=PT+Sans:wght@400;700&display=swap" rel="stylesheet">
<style>
  :root {
    --page: #f1f1f1;
    --card-dark: #333333;
    --card-shade: #4a4a4a;
    --orange: #f07b22;
    --white: #ffffff;
    --grey-text: #8a8a8a;
    --navy: #1f2a5c;
  }
  html, body {
    margin: 0;
    width: 1200px;
    height: 1200px;
    overflow: hidden;
    background: var(--page);
    font-family: "PT Sans", sans-serif;
  }
  .canvas { position: relative; width: 1200px; height: 1200px; }
  .card { position: absolute; display: block; }
  .card--front { left: 256px; top: 166px; }
  .card--back { left: 250px; top: 636px; }
  .brand-name { font-family: "PT Sans", sans-serif; font-weight: 700; fill: var(--white); }
  .person-name { font-family: "PT Sans", sans-serif; font-weight: 700; fill: var(--orange); }
  .person-title { font-family: "PT Sans", sans-serif; font-weight: 400; fill: var(--grey-text); }
  .contact-line { font-family: "PT Sans", sans-serif; font-weight: 400; fill: var(--white); letter-spacing: 0.5px; }
</style>
</head>
<body>
<main class="canvas">

  <!-- Front side -->
  <svg class="card card--front" width="708" height="392" viewBox="0 0 708 392">
    <defs>
      <clipPath id="front-shape"><rect width="708" height="392" rx="32"/></clipPath>
      <radialGradient id="front-deco" cx="0.6" cy="0.5" r="0.6">
        <stop offset="0" stop-color="#484848"/>
        <stop offset="1" stop-color="#333333"/>
      </radialGradient>
    </defs>
    <g clip-path="url(#front-shape)">
      <rect class="card-base" width="708" height="392" fill="var(--card-dark)"/>
      <rect role="img" aria-label="Faint oversized mascot artwork in the background" x="0" y="0" width="708" height="392" fill="url(#front-deco)"/>
    </g>
    <g class="brand-lockup">
      <circle cx="200" cy="192" r="52" fill="var(--navy)"/>
      <text class="brand-name" x="286" y="186" font-size="38">Northbay Play</text>
      <text class="brand-name" x="286" y="226" font-size="38">Careers</text>
    </g>
  </svg>

  <!-- Back side -->
  <svg class="card card--back" width="716" height="397" viewBox="0 0 716 397">
    <defs>
      <clipPath id="back-shape"><rect width="716" height="397" rx="32"/></clipPath>
      <radialGradient id="back-deco" cx="0.35" cy="0.4" r="0.6">
        <stop offset="0" stop-color="#474747"/>
        <stop offset="1" stop-color="#333333"/>
      </radialGradient>
    </defs>
    <g clip-path="url(#back-shape)">
      <rect class="card-base" width="716" height="397" fill="var(--card-dark)"/>
      <rect role="img" aria-label="Faint oversized mascot artwork in the background" x="0" y="0" width="500" height="397" fill="url(#back-deco)"/>
      <!-- white info panel with orange edge -->
      <polygon class="edge-stripe" points="498,0 716,0 716,397 370,397" fill="var(--orange)"/>
      <polygon class="info-panel" points="510,0 716,0 716,397 382,397" fill="var(--white)"/>

      <!-- contact bars -->
      <g class="contact-bars" fill="var(--orange)">
        <polygon points="444,200 474,200 464,232 434,232"/>
        <polygon points="482,200 716,200 716,232 472,232"/>
        <polygon points="428,248 462,248 451,284 417,284"/>
        <polygon points="470,248 716,248 716,284 459,284"/>
        <polygon points="412,292 445,292 434,328 401,328"/>
        <polygon points="453,292 716,292 716,328 442,328"/>
        <polygon points="368,337 716,337 716,370 358,370"/>
      </g>
    </g>

    <!-- icons -->
    <g class="icon icon--phone" fill="var(--white)">
      <path d="M441,206 l4,-1 3,6 -3,2 c1,3 3,6 6,8 l2,-3 6,3 -1,4 c-8,1 -17,-9 -17,-19z"/>
    </g>
    <g class="icon icon--mobile" fill="none" stroke="var(--white)" stroke-width="2">
      <rect x="428" y="254" width="12" height="22" rx="2"/>
      <line x1="432" y1="272" x2="436" y2="272"/>
    </g>
    <g class="icon icon--mail" fill="none" stroke="var(--white)" stroke-width="2">
      <rect x="407" y="302" width="24" height="15"/>
      <polyline points="407,302 419,312 431,302"/>
    </g>

    <!-- contact text -->
    <text class="contact-line" x="689" y="223" font-size="19" text-anchor="end">+44 1632 960418</text>
    <text class="contact-line" x="689" y="273" font-size="20" text-anchor="end">+44 7700 900276</text>
    <text class="contact-line" x="689" y="317" font-size="18" text-anchor="end">darren@nbpc2go.example</text>
    <text class="contact-line" x="689" y="360" font-size="18" text-anchor="end">www.nbpc2go.example</text>

    <!-- name and role -->
    <text class="person-name" x="689" y="54" font-size="34" text-anchor="end">Darren Elsby</text>
    <text class="person-title" x="689" y="80" font-size="21" text-anchor="end">CEO</text>

    <!-- vertical brand lockup -->
    <g class="brand-lockup brand-lockup--vertical">
      <text class="brand-name" font-size="30" transform="translate(178,240) rotate(-90)">Northbay Play</text>
      <text class="brand-name" font-size="30" transform="translate(208,240) rotate(-90)">Careers</text>
      <circle cx="174" cy="306" r="40" fill="var(--navy)"/>
    </g>
  </svg>

</main>
</body>
</html>
```